Package Design for Chew Bone Guild for Marketora

Would like a label to put on a 6x9 package.

Here is my site: chewboneguild.example

Here are the labels I like:
https://rolfandkit.example/collections/bully-sticks/products/6-inch-standard-bully-sticks
https://www.marketora.example/stores/Rolf+%26+Kit/page/A1B2C3D4-5E6F-47A8-9B0C-1D2E3F4A5B6C?ref_=ast_bln
https://quiet-meadowland.example/amber-hound-junior-bully-sticks-6-25-pack/
https://www.wagsandwhimsy.example/shop/open-trailer-bully-stix

```html
<!DOCTYPE html>
<html lang="en">
<head>
<meta charset="utf-8">
<title>Chew Bone Guild — Bully Sticks Pouch Label</title>
<link rel="stylesheet" href="https://fonts.googleapis.com/css2?family=Bowlby+One&family=Arvo:wght@700&family=Zilla+Slab:wght@700&display=swap">
<style>
  :root {
    --page-bg: #f2f2f3;
    --silver-light: #e4e5e7;
    --silver-dark: #c9cacd;
    --leaf-green: #78a043;
    --leaf-green-deep: #6e9a3c;
    --clay-brown: #8e5b4c;
    --clay-band: #93624f;
    --ink: #1d1a19;
    --paper: #ffffff;
  }
  * { margin: 0; padding: 0; box-sizing: border-box; }
  html, body { width: 1200px; height: 1078px; overflow: hidden; background: var(--page-bg); }
  .canvas { position: relative; width: 1200px; height: 1078px; }
  .pouch-label { position: absolute; left: 270px; top: 19px; width: 661px; height: 1040px; }
  .brand-name { font-family: "Arvo", serif; font-weight: 700; font-size: 27px; fill: var(--clay-brown); }
  .headline { font-family: "Bowlby One", sans-serif; font-size: 150px; }
  .headline-shadow { fill: var(--ink); }
  .headline-face { fill: var(--clay-brown); }
  .subhead { font-family: "Arvo", serif; font-weight: 700; font-size: 56px; fill: var(--leaf-green-deep); }
  .pack-count { font-family: "Bowlby One", sans-serif; fill: var(--paper); }
  .benefit-label { font-family: "Arvo", serif; font-weight: 700; font-size: 7px; fill: var(--clay-brown); }
  .spec-text { font-family: "Zilla Slab", serif; font-weight: 700; fill: var(--paper); }
  .grass-fed { font-family: "Zilla Slab", serif; font-weight: 700; font-size: 15px; fill: var(--ink); }
</style>
</head>
<body>
<div class="canvas">
  <svg class="pouch-label" viewBox="0 0 661 1040" xmlns="http://www.w3.org/2000/svg">
    <defs>
      <linearGradient id="silverFoil" x1="0" y1="0" x2="1" y2="0">
        <stop offset="0" stop-color="var(--silver-dark)"/>
        <stop offset="0.5" stop-color="var(--silver-light)"/>
        <stop offset="1" stop-color="var(--silver-dark)"/>
      </linearGradient>
      <linearGradient id="stickTones" x1="0" y1="0" x2="1" y2="1">
        <stop offset="0" stop-color="#a0623c"/>
        <stop offset="1" stop-color="#8a6a2c"/>
      </linearGradient>
    </defs>

    <rect class="panel-white" width="661" height="1040" fill="var(--paper)"/>
    <rect class="foil-top" width="661" height="200" fill="url(#silverFoil)"/>

    <path class="green-band" d="M0 166 C120 140 200 95 330 88 C460 95 560 135 661 160 L661 267 L560 262 L470 272 L380 266 L270 280 L150 288 L60 300 L0 328 Z" fill="var(--leaf-green)"/>
    <path class="green-band-edge" d="M0 166 C120 140 200 95 330 88 C460 95 560 135 661 160" fill="none" stroke="var(--clay-brown)" stroke-width="6"/>

    <g class="brand-badge">
      <circle cx="332" cy="158" r="104" fill="var(--paper)" stroke="var(--ink)" stroke-width="2.5"/>
      <text class="brand-name" x="332" y="150" text-anchor="middle">Chew Bone</text>
      <text class="brand-name" x="332" y="184" text-anchor="middle">Guild</text>
    </g>

    <g class="headline" transform="rotate(-4 340 350)">
      <text class="headline-shadow" x="48" y="440" textLength="572" lengthAdjust="spacingAndGlyphs">BULLY STICKS</text>
      <text class="headline-face" x="60" y="434" textLength="572" lengthAdjust="spacingAndGlyphs">BULLY STICKS</text>
    </g>

    <text class="subhead" x="350" y="498" text-anchor="middle" textLength="300" lengthAdjust="spacingAndGlyphs">All Natural</text>

    <rect class="product-photo" x="95" y="520" width="470" height="200" rx="10" fill="url(#stickTones)" opacity="0.85" role="img" aria-label="Photo of two crossed 6 inch bully sticks"/>

    <g class="pack-badge">
      <circle cx="460" cy="711" r="66" fill="var(--leaf-green)"/>
      <circle cx="460" cy="711" r="57" fill="none" stroke="var(--paper)" stroke-width="4"/>
      <text class="pack-count" x="460" y="712" text-anchor="middle" font-size="44">12</text>
      <text class="pack-count" x="460" y="744" text-anchor="middle" font-size="24">PACK</text>
    </g>

    <path class="brown-band" d="M0 831 L80 822 L170 812 L260 806 L350 800 L440 794 L540 790 L661 785 L661 1040 L0 1040 Z" fill="var(--clay-band)"/>

    <g class="benefit-bubble">
      <path d="M120 792 Q300 770 480 792 Q506 836 480 878 Q300 896 160 880 L110 905 L128 872 Q84 836 120 792 Z" fill="var(--paper)" stroke="var(--ink)" stroke-width="2"/>
      <g class="benefit-icons" fill="none" stroke="var(--clay-brown)" stroke-width="1.5">
        <circle cx="174" cy="832" r="23"/><circle cx="174" cy="832" r="19"/>
        <circle cx="236" cy="832" r="23"/><circle cx="236" cy="832" r="19"/>
        <circle cx="298" cy="832" r="23"/><circle cx="298" cy="832" r="19"/>
        <circle cx="360" cy="832" r="23"/><circle cx="360" cy="832" r="19"/>
        <circle cx="421" cy="832" r="23"/><circle cx="421" cy="832" r="19"/>
      </g>
      <g class="benefit-labels" text-anchor="middle">
        <text class="benefit-label" x="174" y="835" textLength="28" lengthAdjust="spacingAndGlyphs">HEALTH</text>
        <text class="benefit-label" x="236" y="835" textLength="26" lengthAdjust="spacingAndGlyphs">TEETH</text>
        <text class="benefit-label" x="298" y="835" textLength="22" lengthAdjust="spacingAndGlyphs">COAT</text>
        <text class="benefit-label" x="360" y="835" textLength="28" lengthAdjust="spacingAndGlyphs">IMMUNE</text>
        <text class="benefit-label" x="421" y="835" textLength="22" lengthAdjust="spacingAndGlyphs">MIND</text>
      </g>
    </g>

    <rect class="mascot-art" x="81" y="880" width="70" height="100" rx="12" fill="#e9dcd2" role="img" aria-label="Cartoon puppy mascot with brown ears and red collar"/>

    <text class="spec-text" x="489" y="914" text-anchor="middle" font-size="30" textLength="220" lengthAdjust="spacingAndGlyphs">6'' STICK (15,2 cm)</text>

    <g class="grass-fed-box">
      <rect x="483" y="928" width="101" height="85" rx="8" fill="var(--paper)"/>
      <rect x="500" y="938" width="67" height="42" rx="4" fill="#3a3534" role="img" aria-label="Cow silhouette with premium quality mark"/>
      <text class="grass-fed" x="533" y="1003" text-anchor="middle" textLength="84" lengthAdjust="spacingAndGlyphs">100% grass fed</text>
    </g>

    <text class="spec-text" x="340" y="1028" text-anchor="middle" font-size="22" textLength="196" lengthAdjust="spacingAndGlyphs">Net.wt.2,5 oz(70,9 g)</text>
  </svg>
</div>
</body>
</html>
```